Business Card Design

I am an child sleep consultant. I would like the picture to be the background of the card and for my logo to be in the upper right hand corner. Other than that, the design is yours!!

Industry/Entity Type

Business

Contact Information for Business Card

Marla Okonov
Tidewell Nestling
Certified Child Sleep Consultant
(406) 555-0193
tidewellnestling.example

```html
<!DOCTYPE html>
<html lang="en">
<head>
<meta charset="utf-8">
<title>Tidewell Nestling — Business Card</title>
<link rel="stylesheet" href="https://fonts.googleapis.com/css2?family=Didact+Gothic&display=swap">
<style>
  :root {
    --stage: #2a1012;
    --photo-light: #e6e4e2;
    --photo-mid: #a9a6a3;
    --photo-dark: #4a4846;
    --band: rgba(255, 255, 255, 0.88);
    --band-edge: rgba(255, 255, 255, 0.55);
    --teal: #3ea6b9;
    --ink: #2f2f2f;
    --ink-soft: #454545;
  }
  * { box-sizing: border-box; margin: 0; padding: 0; }
  html, body {
    width: 1200px;
    height: 800px;
    overflow: hidden;
    background: var(--stage);
  }
  body {
    font-family: "Didact Gothic", "Century Gothic", sans-serif;
    color: var(--ink);
  }
  .business-card {
    position: absolute;
    left: 75px;
    top: 100px;
    width: 1050px;
    height: 600px;
    overflow: hidden;
    box-shadow: 0 12px 40px rgba(0, 0, 0, 0.5);
  }
  .card-photo {
    position: absolute;
    inset: 0;
    background:
      radial-gradient(ellipse 32% 46% at 42% 52%, var(--photo-light) 0%, #d2d0ce 55%, transparent 100%),
      radial-gradient(ellipse 60% 40% at 70% 12%, #f2f1f0 0%, transparent 80%),
      linear-gradient(160deg, #cfcdcb 0%, var(--photo-mid) 50%, var(--photo-dark) 100%);
  }
  .brand-mark {
    position: absolute;
    top: 40px;
    right: 46px;
    display: flex;
    align-items: center;
    gap: 12px;
  }
  .brand-dot {
    width: 22px;
    height: 22px;
    border-radius: 50%;
    background: var(--teal);
  }
  .brand-name {
    font-size: 30px;
    color: var(--ink);
    letter-spacing: 0.5px;
  }
  .contact-band {
    position: absolute;
    left: 640px;
    right: 0;
    top: 225px;
    height: 200px;
    padding: 22px 40px 0 38px;
    background: linear-gradient(90deg, var(--band-edge) 0%, var(--band) 18%, var(--band) 100%);
  }
  .person-name {
    font-size: 38px;
    color: var(--teal);
    line-height: 1.1;
  }
  .person-title {
    font-size: 20px;
    color: var(--ink-soft);
    margin-top: 6px;
  }
  .contact-list {
    list-style: none;
    margin-top: 18px;
  }
  .contact-item {
    display: flex;
    align-items: center;
    gap: 10px;
    font-size: 29px;
    line-height: 1.25;
    color: var(--ink);
  }
  .contact-item.web { font-size: 26px; }
  .contact-icon {
    width: 24px;
    height: 24px;
    flex: none;
  }
</style>
</head>
<body>
  <article class="business-card">
    <div class="card-photo" role="img" aria-label="Black and white portrait photograph of a smiling baby looking upward, outdoors with soft blurred trees behind"></div>

    <div class="brand-mark">
      <span class="brand-dot"></span>
      <span class="brand-name">Tidewell Nestling</span>
    </div>

    <section class="contact-band">
      <h1 class="person-name">Marla Okonov</h1>
      <p class="person-title">Certified Child Sleep Consultant</p>
      <ul class="contact-list">
        <li class="contact-item phone">
          <svg class="contact-icon" viewBox="0 0 24 24" aria-hidden="true">
            <path fill="var(--teal)" d="M6.6 10.8a15.2 15.2 0 0 0 6.6 6.6l2.2-2.2a1 1 0 0 1 1-.25 11.4 11.4 0 0 0 3.6.57 1 1 0 0 1 1 1V20a1 1 0 0 1-1 1A17 17 0 0 1 3 4a1 1 0 0 1 1-1h3.5a1 1 0 0 1 1 1c0 1.25.2 2.45.57 3.57a1 1 0 0 1-.25 1z"/>
          </svg>
          (406) 555-0193
        </li>
        <li class="contact-item web">
          <svg class="contact-icon" viewBox="0 0 24 24" aria-hidden="true">
            <g fill="none" stroke="var(--teal)" stroke-width="1.8">
              <circle cx="12" cy="12" r="9.5"/>
              <ellipse cx="12" cy="12" rx="4.2" ry="9.5"/>
              <line x1="2.5" y1="12" x2="21.5" y2="12"/>
              <path d="M4.5 7h15M4.5 17h15"/>
            </g>
          </svg>
          tidewellnestling.example
        </li>
      </ul>
    </section>
  </article>
</body>
</html>
```